Upcoming Importing and Distribution Business Needs A Packaging Design!

We are an importing and distribution company that is importing reams of paper into New Zealand; now we have confirmed the product we need a design mocked up for the reams of paper!

We need packaging for the individual reams and then also the box that will hold 5 reams.

Each ream needs to have information on it, including:
A4 Size
500 sheets
80g/m2
Home and Office Use

(On the back of the product) Company contact information
Harrowfield Traders Limited
PO Box 4627
Christchurch 8140
New Zealand
(Email) office@harrowfieldtraders.example.

It is being brought in by our company, Harrowfield Traders (logo attached)

We can't have too many colours in the design as it drives the price up very quickly.

Target Market(s)

Businesses and people that use paper to print documents

Industry/Entity Type

Retail

Requirements
Must have
• Clear simplistic labelling, be eye catching and stand out.
Should not have
• Not too many colours, will drive the price up too much

```html
<!DOCTYPE html>
<html lang="en">
<head>
<meta charset="utf-8">
<title>Harrowfield Traders – A4 Paper Ream Packaging</title>
<link rel="stylesheet" href="https://fonts.googleapis.com/css2?family=Questrial&display=swap">
<style>
  :root {
    --paper-white: #ffffff;
    --canvas-bg: #f2f2f2;
    --brand-yellow: #fbb61b;
    --pattern-yellow: #f7a81a;
    --brand-red: #d7232d;
    --ink: #1b1b1b;
  }
  html, body {
    margin: 0;
    padding: 0;
    width: 1200px;
    height: 1000px;
    overflow: hidden;
    background: var(--canvas-bg);
  }
  .artboard {
    position: relative;
    width: 1200px;
    height: 1000px;
  }
  .ream-face, .box-lid {
    position: absolute;
    display: block;
    box-shadow: 0 2px 8px rgba(0,0,0,0.12);
  }
  .ream-face { left: 90px; top: 60px; }
  .box-lid { left: 760px; top: 620px; }
  .label-text {
    font-family: "Questrial", "Century Gothic", sans-serif;
  }
  .fill-white { fill: var(--paper-white); }
  .fill-yellow { fill: var(--brand-yellow); }
  .fill-pattern { fill: var(--pattern-yellow); }
  .fill-red { fill: var(--brand-red); }
  .fill-ink { fill: var(--ink); }
  .stroke-yellow { stroke: var(--brand-yellow); }
  .stroke-red { stroke: var(--brand-red); }
</style>
</head>
<body>
<main class="artboard">

  <!-- Ream wrapper, front panel -->
  <svg class="ream-face" width="620" height="880" viewBox="0 0 620 880" aria-label="A4 paper ream front panel">
    <rect class="fill-white" x="0" y="0" width="620" height="880"/>

    <g class="size-corner">
      <polygon class="fill-pattern" points="0,0 620,0 0,340" role="img" aria-label="Yellow corner panel with repeating zigzag pattern"/>
      <text class="label-text fill-white" x="70" y="150" font-size="92">A4</text>
    </g>

    <g class="brand-mark">
      <text class="label-text fill-ink" x="465" y="468" font-size="36" text-anchor="end" textLength="340" lengthAdjust="spacingAndGlyphs">Harrowfield Traders</text>
      <circle cx="515" cy="456" r="30" fill="none" class="stroke-red" stroke-width="2.5"/>
    </g>

    <g class="spec-bands">
      <rect class="fill-yellow" x="0" y="580" width="620" height="80"/>
      <text class="label-text fill-white" x="110" y="632" font-size="32">500 Sheets</text>

      <rect class="fill-red" x="0" y="682" width="620" height="72"/>
      <line class="stroke-yellow" x1="0" y1="740" x2="620" y2="740" stroke-width="4"/>
      <text class="label-text fill-white" x="140" y="725" font-size="30">80 g/m2</text>

      <text class="label-text fill-ink" x="140" y="822" font-size="30">Home and Office Use</text>
    </g>
  </svg>

  <!-- Five-ream box, lid top -->
  <svg class="box-lid" width="400" height="290" viewBox="0 0 400 290" aria-label="Five ream box lid">
    <rect class="fill-white" x="0" y="0" width="400" height="290"/>

    <rect class="fill-pattern" x="0" y="0" width="140" height="290" role="img" aria-label="Yellow panel with repeating zigzag pattern"/>
    <text class="label-text fill-white" font-size="40" transform="translate(84 170) rotate(-90)">A4</text>

    <g class="brand-mark" transform="translate(206 130) rotate(-90)">
      <text class="label-text fill-ink" x="0" y="0" font-size="16" text-anchor="middle" textLength="140" lengthAdjust="spacingAndGlyphs">Harrowfield Traders</text>
      <circle cx="90" cy="-5" r="10" fill="none" class="stroke-red" stroke-width="1.5"/>
    </g>

    <rect class="fill-yellow" x="265" y="0" width="40" height="290"/>
    <text class="label-text fill-white" font-size="15" transform="translate(290 185) rotate(-90)">500 Sheets</text>

    <rect class="fill-red" x="318" y="0" width="30" height="290"/>
    <line class="stroke-yellow" x1="340" y1="0" x2="340" y2="290" stroke-width="2"/>
    <text class="label-text fill-white" font-size="12" transform="translate(334 172) rotate(-90)">80 g/m2</text>

    <text class="label-text fill-ink" font-size="12" transform="translate(378 202) rotate(-90)">Home and Office Use</text>
  </svg>

</main>
</body>
</html>
```